Kiswa Design

We need a flyer design for a product that we are a selling, a sacred Islamic cloth called a Kiswah, which is draped around the holy Kaaba in mecca every year.

The details we would like on the flyer are as follows:

Rare Kiswah of the holy Kaaba for sale (fitted in 1977 and 1982 vintage). For sale:

1) whole piece 15 meters x 2.60 meters : £60,000
2) 8 meters x 2.60 meters : £31,200
3) 4 meters x 2.60 meters : £15,600
4) 1 meter : £1500

(insert a high quality picture of holy Kaaba here, then underneath the picture, write the following:) "The Kaaba is covered by an expensive black cloth which is known as 'Kiswah' which is produced and changed every year"

(insert picture of our product here,i.e. use the document named MAIN IMAGE then underneath this picture write the following:) "Silk lampas weave Kiswah, woven silk on a black satin ground with Quranic calligraphy, the zig-zag bands of inscription alternate with the Shahadah and the inscription, 'God, exalted be His Glory!"

insert another picture of kiswah which i provided anywhere you like

(somewhere on flyer write the following) please note a percentage of sales will go towards Sadaqah for our Muslim brothers and sisters in need around the world

(somewhere on flyer write the following) Hallorand's international auction house authenticity document also available to prove the Kiswah is genuine.

100% genuine

contact us today! deals this good don't last forever.

email: relicoffer@tarnwickmail.com

Please use the images that I have attached on the flyer accordingly. Also feel free to be as creative as possible I want it to attract a lot of attention but also look professional so you may add some things to improve the look of the flyer.

note: the product being sold is on the pictures I've provided, in particular, i want file 2 "main image" in a large size on the flyer!

thank you! and happy holidays

Muslims and Islamic collectors

House

• the dimensions of the flyer is :
• A5 horizontal or vertical
• (210 x 148 mm)
• must have colors! up to you what colors to choose!

```html
<!DOCTYPE html>
<html lang="en">
<head>
<meta charset="utf-8">
<title>Rare Kiswah of the Holy Kaaba – Flyer</title>
<link rel="stylesheet" href="https://fonts.googleapis.com/css2?family=Bebas+Neue&family=Arimo:ital,wght@0,400;0,700;1,400;1,700&display=swap">
<style>
  :root {
    --stage: #e4e4e4;
    --ink: #231f20;
    --white: #ffffff;
    --muted: #8a8a8a;
    --price: #ffe400;
    --violet: #7b2d8e;
    --violet-band: #858585;
    --green: #6cbb45;
    --green-deep: #1f6e36;
    --green-band: #1d6a32;
    --strip-yellow: #ffe600;
  }
  * { box-sizing: border-box; margin: 0; padding: 0; }
  html, body { width: 1200px; height: 689px; overflow: hidden; }
  body {
    background: var(--stage);
    position: relative;
    font-family: "Arimo", Arial, sans-serif;
  }
  .flyer {
    position: absolute;
    top: 76px;
    width: 369px;
    height: 524px;
    background: var(--ink);
    overflow: hidden;
    box-shadow: 0 6px 18px rgba(0,0,0,.18);
  }
  .flyer--violet { left: 162px; --accent: var(--violet); --band: var(--violet-band); --box: var(--violet); --strip: var(--strip-yellow); --strip-text: var(--ink); --footer: var(--ink); --note: #e8d6ee; }
  .flyer--green  { left: 672px; --accent: var(--green); --band: var(--green-band); --box: var(--green); --strip: var(--green-deep); --strip-text: var(--white); --footer: var(--green-deep); --note: #1d5a2a; }

  .flyer__title {
    position: absolute; left: 25px; top: 17px;
    font-family: "Bebas Neue", Impact, sans-serif;
    font-size: 33px; line-height: 1; color: var(--white); letter-spacing: .2px;
  }
  .flyer__sale {
    position: absolute; left: 25px; top: 45px;
    font-family: "Bebas Neue", Impact, sans-serif;
    font-size: 60px; line-height: 1; color: var(--accent);
  }
  .flyer__vintage {
    position: absolute; left: 208px; top: 49px;
    font-size: 17px; line-height: 23px; color: var(--muted);
  }
  .photo {
    position: absolute;
    background: linear-gradient(160deg, #5c5c5c 0%, #2a2a2a 45%, #111 100%);
  }
  .photo--main { left: 7px; top: 109px; width: 226px; height: 314px; }
  .flyer--green .photo--main { background: radial-gradient(ellipse at 45% 40%, #9a9a9a 0%, #5a5a5a 45%, #262626 100%); }
  .photo--detail { left: 239px; top: 267px; width: 130px; height: 156px;
    background: linear-gradient(90deg, #1a1a1a 0 10px, #b89a3a 10px 16px, #2b2b2b 16px 100%); }
  .caption {
    position: absolute; color: var(--white);
    font-size: 8.6px; line-height: 10.6px; font-style: italic; text-align: right;
    text-shadow: 0 0 3px rgba(0,0,0,.8);
  }
  .caption--main { right: 136px; top: 381px; width: 175px; }
  .caption--detail { right: 6px; top: 350px; width: 118px; }
  .caption b { font-weight: 700; }

  .prices {
    position: absolute; left: 239px; top: 110px; width: 130px; height: 151px;
    background: var(--box); color: var(--white);
  }
  .prices__head {
    margin-top: 3px; height: 24px; background: var(--band);
    font-family: "Bebas Neue", Impact, sans-serif; font-size: 21px; line-height: 26px;
    padding-left: 8px;
  }
  .prices__list { list-style: none; padding: 5px 0 0 9px; font-size: 10.4px; }
  .prices__list li { margin-bottom: 7px; }
  .prices__list .sub { display: block; padding-left: 13px; font-size: 9px; margin-top: 1px; }
  .prices__list strong { color: var(--price); }
  .prices__note { padding: 0 5px 0 9px; font-size: 6.3px; line-height: 7.5px; font-style: italic; color: var(--note); margin-top: -2px; }

  .strip {
    position: absolute; left: 0; top: 423px; width: 369px; height: 14px;
    background: var(--strip); color: var(--strip-text);
    font-size: 6.4px; line-height: 14px; padding-left: 23px;
  }
  .footer { position: absolute; left: 0; top: 437px; width: 369px; height: 87px; background: var(--footer); }
  .footer__genuine {
    position: absolute; left: 24px; top: 12px;
    font-family: "Bebas Neue", Impact, sans-serif; font-size: 35px; line-height: 1; color: var(--white);
  }
  .footer__divider { position: absolute; left: 195px; top: 15px; width: 1px; height: 30px; background: var(--white); }
  .footer__cta {
    position: absolute; left: 208px; top: 12px;
    font-family: "Bebas Neue", Impact, sans-serif; font-size: 19px; line-height: 1; color: var(--price);
  }
  .footer__tag { position: absolute; left: 208px; top: 31px; font-size: 8.3px; color: var(--white); }
  .footer__email {
    position: absolute; left: 0; width: 369px; top: 52px;
    display: flex; justify-content: center; align-items: center; gap: 6px;
    font-family: "Bebas Neue", Impact, sans-serif; font-size: 16px; color: var(--white); letter-spacing: .2px;
  }
</style>
</head>
<body>

<article class="flyer flyer--violet">
  <h1 class="flyer__title">Rare Kiswah of the Holy Kaaba</h1>
  <p class="flyer__sale">For Sale</p>
  <p class="flyer__vintage">(Fitted in1977 and<br>1982 Vintage)</p>
  <div class="photo photo--main" role="img" aria-label="Photo of the folded black Kiswah cloth"></div>
  <p class="caption caption--main">The <b>Kaaba</b> is covered by an expensive black cloth which is known as 'Kiswah' which is produced and changed every year</p>
  <section class="prices">
    <h2 class="prices__head">For Sale*:</h2>
    <ol class="prices__list">
      <li>1) Whole piece<span class="sub">15m x 2.60m: <strong>£60,000</strong></span></li>
      <li>2) 8 m x 2.60 m: <strong>£31,200</strong></li>
      <li>3) 4 m x 2.60 m: <strong>£15,600</strong></li>
      <li>4) 1 meter: <strong>£1500</strong></li>
    </ol>
    <p class="prices__note">* A percentage of sales will go towards Sadaqah for our Muslim brothers and sisters in need around the world.</p>
  </section>
  <div class="photo photo--detail" role="img" aria-label="Close-up of the Kiswah with gold calligraphy band"></div>
  <p class="caption caption--detail"><b>Silk lampas weave Kiswah</b>, woven silk on a black satin ground with Quranic calligraphy, the zig-zag bands of inscription alternate with the Shahadah and the inscription, 'God, exalted be His Glory!</p>
  <p class="strip">• Hallorand's international auction house authenticity document also available to prove the Kiswah is genuine.</p>
  <footer class="footer">
    <p class="footer__genuine">100% Genuine</p>
    <span class="footer__divider"></span>
    <p class="footer__cta">Contact Us Today!</p>
    <p class="footer__tag">Deals This Good Don't Last Forever.</p>
    <p class="footer__email">
      <svg width="20" height="14" viewBox="0 0 20 14" aria-hidden="true"><rect x="1" y="1" width="18" height="12" fill="#ffe400" transform="rotate(-8 10 7)"/><path d="M2 2 L10 8 L18 0" stroke="#231f20" stroke-width="1.2" fill="none" transform="rotate(-8 10 7)"/></svg>
      relicoffer@tarnwickmail.com
    </p>
  </footer>
</article>

<article class="flyer flyer--green">
  <h1 class="flyer__title">Rare Kiswah of the Holy Kaaba</h1>
  <p class="flyer__sale">For Sale</p>
  <p class="flyer__vintage">(Fitted in1977 and<br>1982 Vintage)</p>
  <div class="photo photo--main" role="img" aria-label="Photo of the Kiswah draped over the Kaaba with woven calligraphy"></div>
  <p class="caption caption--main">The <b>Kaaba</b> is covered by an expensive black cloth which is known as 'Kiswah' which is produced and changed every year</p>
  <section class="prices">
    <h2 class="prices__head">For Sale*:</h2>
    <ol class="prices__list">
      <li>1) Whole piece<span class="sub">15m x 2.60m: <strong>£60,000</strong></span></li>
      <li>2) 8 m x 2.60 m: <strong>£31,200</strong></li>
      <li>3) 4 m x 2.60 m: <strong>£15,600</strong></li>
      <li>4) 1 meter: <strong>£1500</strong></li>
    </ol>
    <p class="prices__note">* A percentage of sales will go towards Sadaqah for our Muslim brothers and sisters in need around the world.</p>
  </section>
  <div class="photo photo--detail" role="img" aria-label="Close-up of the Kiswah with gold calligraphy band"></div>
  <p class="caption caption--detail"><b>Silk lampas weave Kiswah</b>, woven silk on a black satin ground with Quranic calligraphy, the zig-zag bands of inscription alternate with the Shahadah and the inscription, 'God, exalted be His Glory!</p>
  <p class="strip">• Hallorand's international auction house authenticity document also available to prove the Kiswah is genuine.</p>
  <footer class="footer">
    <p class="footer__genuine">100% Genuine</p>
    <span class="footer__divider"></span>
    <p class="footer__cta">Contact Us Today!</p>
    <p class="footer__tag">Deals This Good Don't Last Forever.</p>
    <p class="footer__email">
      <svg width="20" height="14" viewBox="0 0 20 14" aria-hidden="true"><rect x="1" y="1" width="18" height="12" fill="#ffe400" transform="rotate(-8 10 7)"/><path d="M2 2 L10 8 L18 0" stroke="#1f6e36" stroke-width="1.2" fill="none" transform="rotate(-8 10 7)"/></svg>
      relicoffer@tarnwickmail.com
    </p>
  </footer>
</article>

</body>
</html>
```